Web Design Project - Quillmore Analytics

I am a Mechanical Engineer running a one person consulting firm at this point. The hope is to expand in the future, but for now I simply need a website that conveys a professional appearance, and allows potential and existing clients to find me. Website design displaying contact information, CV for download, capabilities, past projects, etc. I've included four examples below from companies that provided the same service. I've only provided these as general reference for the type of work I do and how others have chosen to display this information. The design is completely at your discretion.

I've included the current Logo in the uploaded files section. I will provide content as requried.

http://www.torvanmech.com/
http://www.halberic.com/
http://www.rumblaxsystems.com/
http://dorwickmotive.net/

Industry/Entity Type

Consulting

```html
<!DOCTYPE html>
<html lang="en">
<head>
<meta charset="utf-8">
<title>Quillmore Analytics – Engineering Consultants</title>
<link rel="stylesheet" href="https://fonts.googleapis.com/css2?family=Oswald:wght@400;500&family=Source+Sans+3:wght@300;400;600&display=swap">
<style>
:root{
  --orange:#e07f2c;
  --orange-light:#f39a45;
  --orange-dark:#d06d1c;
  --ink:#2f2f2f;
  --heading:#555;
  --text:#6b6b6b;
  --line:#dedede;
  --footer:#f3f3f3;
  --photo-a:#c9ccd2;
  --photo-b:#8a93a3;
}
*{box-sizing:border-box;margin:0;padding:0}
html,body{width:1065px;height:1200px;overflow:hidden;background:#fff}
body{position:relative;font-family:"Source Sans 3",sans-serif;color:var(--text)}
.abs{position:absolute;white-space:nowrap}

/* header */
.brand{left:64px;top:28px;display:flex;align-items:center;gap:10px}
.brand-mark{width:22px;height:22px;background:var(--orange)}
.brand-name{font-family:"Source Sans 3",sans-serif;font-weight:600;font-size:21px;color:var(--orange);letter-spacing:1px;text-transform:uppercase}
.brand-tag{left:96px;top:57px;font-size:9px;letter-spacing:1.5px;color:#555;text-transform:uppercase;font-weight:600}
.social{left:700px;top:19px;display:flex;gap:8px}
.social span{width:24px;height:24px;border-radius:50%;background:#6a6a6a}
.search{left:794px;top:18px;width:209px;height:28px;border:1px solid #d4d4d4;border-radius:14px;font-size:12px;font-style:italic;color:#999;padding:6px 13px;font-weight:300}
.search svg{position:absolute;right:9px;top:7px}
.nav{left:443px;top:59px;width:562px;height:48px}
.nav-links{left:0;top:0;width:562px;height:48px;display:flex;align-items:center;padding-left:24px;list-style:none}
.nav-links li{color:#fff;font-size:16.5px;padding:0 15.5px;border-left:1px solid rgba(255,255,255,.45);line-height:18px;white-space:nowrap}
.nav-links li:first-child{border-left:none}

/* hero */
.hero{left:0;top:107px;width:1058px;height:396px;background:linear-gradient(100deg,#e9e6e2 0%,var(--photo-a) 35%,#a7b0bf 60%,var(--photo-b) 80%,#d8c2ad 100%)}
.hero-panel{left:0;top:318px}
.hero-kicker{left:73px;top:334px;font-family:"Oswald",sans-serif;font-weight:500;font-size:26px;color:var(--orange);letter-spacing:-.3px}
.hero-title{left:68px;top:361px;font-family:"Oswald",sans-serif;font-weight:500;font-size:47px;color:var(--ink);letter-spacing:.5px}
.hero-text{left:72px;top:423px;width:300px;font-size:12.5px;line-height:17px;color:#444;font-weight:400;white-space:normal}
.hero-arrows{left:925px;top:452px}

/* sections */
.h-section{font-family:"Oswald",sans-serif;font-weight:500;font-size:20px;color:var(--heading);letter-spacing:-.2px}
.photo{background:linear-gradient(135deg,#c7ccd3,#6f7784)}
.project{top:582px;width:201px}
.project .photo{height:103px}
.project h3{font-weight:400;font-size:13.5px;color:#444;margin-top:11px}
.project p{font-weight:300;font-size:12.5px;line-height:18px;color:var(--text);margin-top:2px}
.cap-text{left:765px;top:695px;width:235px;font-size:12.5px;line-height:18.5px;font-weight:300;white-space:normal}
.learn{left:765px;top:755px;font-family:"Oswald",sans-serif;font-size:12px;color:#333;letter-spacing:.2px}
.divider{left:49px;top:803px;width:944px;height:1px;background:var(--line)}
.welcome-title{left:63px;top:832px;font-family:"Oswald",sans-serif;font-weight:500;font-size:23px;color:var(--orange);letter-spacing:-.3px}
.welcome-lead{left:63px;top:873px;font-size:14.5px;color:#444;font-weight:400}
.welcome-body{left:63px;top:899px;width:660px;font-size:12.5px;line-height:20.5px;font-weight:300;white-space:normal}
.welcome-body p+p{margin-top:13px}
.contact-title{left:766px;top:836px}
.contact{left:767px;top:871px;font-size:13px;line-height:21.2px;color:#333;font-weight:400}
.contact .org{font-size:14px;margin-bottom:2px}
.download{left:766px;top:991px;width:228px;height:40px;border-radius:3px;background:linear-gradient(var(--orange-light),var(--orange-dark));color:#fff;font-family:"Oswald",sans-serif;font-size:18px;letter-spacing:.4px;padding:6px 0 0 20px}
.download svg{position:absolute;right:14px;top:8px}

/* footer */
.footer{left:0;top:1113px;width:1065px;height:87px;background:linear-gradient(#f7f7f7,#fff)}
.footer-nav{left:66px;top:1143px;font-size:15px;color:#333;word-spacing:2px}
.footer-nav span{color:#777;margin:0 8px}
.copyright{right:85px;top:1146px;font-size:12px;color:#666;font-weight:300}
</style>
</head>
<body>

<header>
  <div class="abs brand"><span class="brand-mark"></span><span class="brand-name">Quillmore Analytics</span></div>
  <div class="abs brand-tag">Engineering Consultants</div>
  <div class="abs social" aria-label="Social links"><span></span><span></span><span></span></div>
  <div class="abs search">Search here..
    <svg width="14" height="14" viewBox="0 0 14 14"><circle cx="6" cy="6" r="4.5" fill="none" stroke="#999" stroke-width="2"/><line x1="9.3" y1="9.3" x2="13" y2="13" stroke="#999" stroke-width="2"/></svg>
  </div>
  <nav class="abs nav">
    <svg class="abs" width="562" height="48" viewBox="0 0 562 48" style="left:0;top:0">
      <defs><linearGradient id="navGrad" x1="0" y1="0" x2="0" y2="1"><stop offset="0" stop-color="#f29a48"/><stop offset="1" stop-color="#e07f2c"/></linearGradient></defs>
      <path d="M16 0H555a5 5 0 0 1 5 5V48H0Q6 4 16 0Z" fill="url(#navGrad)"/>
    </svg>
    <ul class="abs nav-links">
      <li>Main</li><li>About Us</li><li>Download</li><li>Projects</li><li>Services</li><li>Contact</li>
    </ul>
  </nav>
</header>

<section>
  <div class="abs hero" role="img" aria-label="Photo of consultants discussing work around a table"></div>
  <svg class="abs hero-panel" width="420" height="160" viewBox="0 0 420 160">
    <path d="M0 0H415L370 160H0Z" fill="#fff" fill-opacity=".86"/>
  </svg>
  <div class="abs hero-kicker">EXPERIENCE ENGINEERING</div>
  <div class="abs hero-title">CONSULTANTS</div>
  <p class="abs hero-text">Mauris vel lacus vitae felis vestibulum volutpat. Etiam est nunc, venenatis in, tristique eu, imperdiet ac</p>
  <svg class="abs hero-arrows" width="66" height="40" viewBox="0 0 66 40" aria-label="Slide arrows">
    <polyline points="17,2 3,20 17,38" fill="none" stroke="#fff" stroke-width="2"/>
    <polyline points="49,2 63,20 49,38" fill="none" stroke="#fff" stroke-width="2"/>
  </svg>
</section>

<section>
  <h2 class="abs h-section" style="left:63px;top:544px">PAST PROJECTS</h2>
  <article class="abs project" style="left:61px">
    <div class="photo" role="img" aria-label="Photo of two colleagues in a meeting"></div>
    <h3>Phasellus felis dolor</h3>
    <p>Scelerisque a, tempus eget,<br>lobortis id, libero.</p>
  </article>
  <article class="abs project" style="left:277px">
    <div class="photo" role="img" aria-label="Photo of a team around a laptop"></div>
    <h3>Phasellus felis dolor</h3>
    <p>Scelerisque a, tempus eget,<br>lobortis id, libero.</p>
  </article>
  <article class="abs project" style="left:493px">
    <div class="photo" role="img" aria-label="Photo of a boardroom meeting"></div>
    <h3>Phasellus felis dolor</h3>
    <p>Scelerisque a, tempus eget,<br>lobortis id, libero.</p>
  </article>
  <svg class="abs" style="left:655px;top:749px" width="32" height="20" viewBox="0 0 32 20" aria-label="Project arrows">
    <polyline points="10,1 2,10 10,19" fill="none" stroke="#555" stroke-width="1.6"/>
    <polyline points="22,1 30,10 22,19" fill="none" stroke="#555" stroke-width="1.6"/>
  </svg>

  <div class="abs photo" style="left:765px;top:541px;width:240px;height:117px" role="img" aria-label="Photo of a business team at a meeting table"></div>
  <h2 class="abs h-section" style="left:766px;top:664px">CAPABILITIES</h2>
  <p class="abs cap-text">Phasellus felis dolor, scelerisque a, tempus eget, lobortis id, libero. Donec scelerisque leo ac risus. Praesent sit amet est.</p>
  <div class="abs learn">LEARN MORE ▸</div>
</section>

<div class="abs divider"></div>

<section>
  <h1 class="abs welcome-title">WELCOME TO OUR WEBSITE MAINPAGE</h1>
  <p class="abs welcome-lead">Maecenas aliquet velit vel turpis. Mauris neque metus, malesuada nec</p>
  <div class="abs welcome-body">
    <p>Nunc tempus felis vitae urna. Vivamus porttitor, g, purus nisi eleifend libero, a tempus libero lectus feugiat felis. Morbi diam mauris, viverra in, gravida eu, mattis in, ante. Morbi eget arcu. Morbi porta, libero id ullamcorper nonummy, nibh ligula pulvinar metus, eget consectetuer augue nisi quis lacus.</p>
    <p>Phasellus felis dolor, scelerisque a, tempus eget, lobortis id, libero. Donec scelerisque leo ac risus. Praesent sit amet est. In dictum, dolor eu dictum porttitor, enim felis viverra mi, eget luctus massa purus quis odio. Etiam nulla massa, pharetra facilisis, volutpat in, imperdiet sit amet, sem</p>
  </div>

  <h2 class="abs h-section contact-title">CONTACT INFO</h2>
  <address class="abs contact" style="font-style:normal">
    <div class="org">Quillmore Analytics</div>
    48 Harlow Lane #4B<br>
    Brookfield 20931 NY<br>
    Tele +1 (555) 014-2290<br>
    Email : info@quillmoreanalytics.com
  </address>
  <div class="abs download">Download Resume
    <svg width="26" height="26" viewBox="0 0 26 26"><circle cx="13" cy="13" r="11" fill="none" stroke="#fff" stroke-width="2.5"/><path d="M13 6v10M8.5 12l4.5 5 4.5-5" fill="none" stroke="#fff" stroke-width="2.5"/></svg>
  </div>
</section>

<footer>
  <div class="abs footer"></div>
  <nav class="abs footer-nav">Main<span>/</span>About Us<span>/</span>Download<span>/</span>Projects<span>/</span>Services<span>/</span>Contact</nav>
  <div class="abs copyright">© 2013 Company Name.&nbsp; All right reserved.&nbsp; Term of Use</div>
</footer>

</body>
</html>
```